VENTURE CAPITAL GROUP BUSINESS CARD DESIGN

Venture Capital Group based in SF looking for a bold business card design. No trendy colour explosion, 3D effects etc. Just "simple" optical effects. Works on your brain, keeps your eye focused and sticks to your mind.
Target Market(s)
Technology startups
Industry/Entity Type
Venture Capital
Contact Information for Business Card
BARNABY WHITLOCK
MANAGING PARTNER
817 FERN ST SAN FRANCISCO, CA 94111
415.555.0143 O
415.555.0167 F
415.555.0192 C
barn@halcyonridgefund.example

```html
<!DOCTYPE html>
<html lang="en">
<head>
<meta charset="utf-8">
<title>Halcyon Ridge Fund – Business Card</title>
<link href="https://fonts.googleapis.com/css2?family=Open+Sans:ital,wght@0,400;0,600;1,400&display=swap" rel="stylesheet">
<style>
  :root {
    --backdrop: #a4a4a4;
    --card-white: #eeeff1;
    --green-deep: #0f4a1a;
    --green-mid: #1c6a2a;
    --green-bright: #2f8a3c;
    --name-green: #1d5a26;
    --ink-grey: #6d6d6d;
    --ink-dark: #3c3c3c;
    --orb: #dcdde0;
  }
  * { box-sizing: border-box; margin: 0; padding: 0; }
  html, body {
    width: 1105px; height: 1200px; overflow: hidden;
    background: var(--backdrop);
    font-family: "Open Sans", Arial, sans-serif;
  }
  .canvas { position: relative; width: 1105px; height: 1200px; }
  .card {
    position: absolute; left: 182px; width: 746px; height: 425px;
    overflow: hidden;
  }
  .card--front { top: 119px; background: var(--card-white); }
  .card--back {
    top: 637px;
    background: radial-gradient(ellipse at 50% 50%, var(--green-bright) 0%, var(--green-mid) 40%, var(--green-deep) 100%);
  }

  /* Front: brand */
  .brand-front { position: absolute; left: 440px; top: 46px; width: 282px; text-align: center; }
  .brand-front .brand-orb {
    width: 104px; height: 104px; border-radius: 50%;
    background: var(--orb); margin: 0 auto 12px;
  }
  .brand-front .brand-name {
    font-size: 25px; font-weight: 400; color: var(--green-mid); letter-spacing: 1px;
  }

  /* Front: person */
  .person { position: absolute; left: 36px; top: 174px; }
  .person-name { font-size: 25px; font-weight: 600; color: var(--name-green); line-height: 1.1; }
  .person-title { font-size: 19px; color: var(--ink-grey); margin-top: 2px; }

  .contact-list { position: absolute; left: 36px; top: 246px; list-style: none; }
  .contact-list li {
    display: flex; align-items: center; height: 29px;
    font-size: 19px; color: var(--ink-dark);
  }
  .contact-list svg { width: 18px; height: 18px; margin-right: 14px; fill: var(--name-green); flex: none; }
  .address { position: absolute; left: 36px; top: 369px; font-size: 19px; color: var(--ink-dark); }

  /* Back */
  .brand-back { position: absolute; left: 0; right: 0; top: 100px; text-align: center; }
  .brand-back .brand-orb {
    width: 150px; height: 150px; border-radius: 50%;
    background: var(--orb); margin: 0 auto 18px;
  }
  .brand-back .brand-name { font-size: 26px; color: #ffffff; letter-spacing: 2px; }
  .web-address {
    position: absolute; left: 0; right: 0; top: 348px; text-align: center;
    font-size: 20px; font-style: italic; color: #e6efe6; letter-spacing: 1.5px;
  }
</style>
</head>
<body>
<div class="canvas">

  <section class="card card--front">
    <div class="brand-front">
      <div class="brand-orb"></div>
      <div class="brand-name">HALCYON RIDGE FUND</div>
    </div>

    <div class="person">
      <div class="person-name">Barnaby Whitlock</div>
      <div class="person-title">Managing Partner</div>
    </div>

    <ul class="contact-list">
      <li>
        <svg viewBox="0 0 24 24" aria-hidden="true"><path d="M6.6 10.8a15.1 15.1 0 0 0 6.6 6.6l2.2-2.2c.3-.3.7-.4 1-.2 1.1.4 2.3.6 3.6.6.6 0 1 .4 1 1V20c0 .6-.4 1-1 1C10.6 21 3 13.4 3 4c0-.6.4-1 1-1h3.5c.6 0 1 .4 1 1 0 1.3.2 2.5.6 3.6.1.3 0 .7-.2 1z"/></svg>
        415.555.0143
      </li>
      <li>
        <svg viewBox="0 0 24 24" aria-hidden="true"><path d="M7 1h10a2 2 0 0 1 2 2v18a2 2 0 0 1-2 2H7a2 2 0 0 1-2-2V3a2 2 0 0 1 2-2zm0 3v14h10V4zm5 15.2a1.1 1.1 0 1 0 0 2.2 1.1 1.1 0 0 0 0-2.2z"/></svg>
        415.555.0192
      </li>
      <li>
        <svg viewBox="0 0 24 24" aria-hidden="true"><path d="M6 2h10l2 2v5H6zM3 10h18a1 1 0 0 1 1 1v8a1 1 0 0 1-1 1H3a1 1 0 0 1-1-1v-8a1 1 0 0 1 1-1zm3 5v5h12v-5z"/></svg>
        415.555.0167
      </li>
      <li>
        <svg viewBox="0 0 24 24" aria-hidden="true"><path d="M2 5h20v14H2zm2 2v.5l8 5.5 8-5.5V7l-8 5.2z"/></svg>
        barn@halcyonridgefund.example
      </li>
    </ul>

    <div class="address">817 Fern ST San Francisco, CA 94111</div>
  </section>

  <section class="card card--back">
    <div class="brand-back">
      <div class="brand-orb"></div>
      <div class="brand-name">HALCYON RIDGE FUND</div>
    </div>
    <div class="web-address">www.halcyonridgefund.example</div>
  </section>

</div>
</body>
</html>
```